Minimalist, Flat(Matte) design for a Beef Jerky packaging company. No bullshit company looking for a

Need a packaging design for a new Beef Jerky product(in English). The name of the company is 'Velmor' and thus the packaging should reflect the bullish, tough, and simple nature of the beef jerky product. The finished product should communicate simplicity, minimalism, yet toughness and strength.

The logo should be simple, with a minimal number of colors , and should be either all white/cream, or have some red as well. Main colors should be white, cream, tinted red, and matte black. I think 4 colors max would be best. The closest example to an existing package style would be Korvanti Dusk clove cigarettes( image attached).

It will be on a matte black standing pouch package. See image for package type. Package dimensions:

Dimension: Width x Gusset x Height
INCH : 5.125" (W) x 3.125" (G) x 8.125" (H)
MILLIMETER : 130mm (W) x 80mm (G) x 205mm (H)

I don't have anything totally specific so artistic liberty is encouraged, provided the colors are kept to a minimum and looks consistent with the simple nature of the brand and the matte black packaging.

Also attached an existing beef jerky package with a similar style to what we're looking for.

Industry/Entity Type

It Company

Colors
f59195
ffffff

Requirements
Must have
• Low contrast, flat and minimalist design.
Should not have
• A complicated design with many colors. Gawdy/flashy design. Bright colors. High contrast.

```html
<!DOCTYPE html>
<html lang="en">
<head>
<meta charset="utf-8">
<title>Velmor Jerky Beef Pouch</title>
<link rel="stylesheet" href="https://fonts.googleapis.com/css2?family=Oswald:wght@500;700&family=Pacifico&display=swap">
<style>
  :root {
    --matte-black: #0d0d0d;
    --tinted-red: #c95c6a;
    --white: #ffffff;
    --backdrop: #ffffff;
  }
  * { margin: 0; padding: 0; box-sizing: border-box; }
  html, body {
    width: 1200px; height: 1200px; overflow: hidden;
    background: var(--backdrop);
  }
  .canvas { position: relative; width: 1200px; height: 1200px; }
  .pouch {
    position: absolute; left: 252px; top: 60px;
    width: 696px; height: 1080px;
    background: var(--matte-black);
    border-left: 28px solid var(--tinted-red);
    border-right: 28px solid var(--tinted-red);
  }
  .brand {
    position: absolute; left: 0; right: 0; top: 262px;
    display: flex; align-items: center; justify-content: center; gap: 22px;
  }
  .brand-dot {
    width: 60px; height: 60px; border-radius: 50%;
    background: var(--tinted-red);
  }
  .brand-name {
    font-family: "Oswald", sans-serif; font-weight: 700;
    font-size: 90px; line-height: 1.1; color: var(--white);
    letter-spacing: 2px;
  }
  .product {
    position: absolute; left: 0; right: 0; top: 490px;
    transform: rotate(-10deg); transform-origin: center;
    text-align: center;
  }
  .product-tagline {
    font-family: "Pacifico", cursive; color: var(--white);
    font-size: 34px; line-height: 1.2;
  }
  .product-name {
    font-family: "Oswald", sans-serif; font-weight: 700;
    color: var(--white); font-size: 112px; line-height: 1.05;
    letter-spacing: 1px; white-space: nowrap;
  }
  .product-flavour {
    display: inline-block; margin-top: 8px; margin-right: 40px;
    background: var(--tinted-red); color: var(--white);
    font-family: "Oswald", sans-serif; font-weight: 500;
    font-size: 24px; line-height: 1; padding: 8px 28px 9px;
    letter-spacing: 0.5px; white-space: nowrap;
  }
  .net-weight {
    position: absolute; left: 0; right: 0; top: 990px;
    text-align: center; color: var(--white);
    font-family: "Oswald", sans-serif; font-weight: 500;
    font-size: 28px; line-height: 1.2; letter-spacing: 0.5px;
  }
</style>
</head>
<body>
  <div class="canvas">
    <div class="pouch">
      <div class="brand">
        <span class="brand-dot"></span>
        <span class="brand-name">Velmor</span>
      </div>
      <div class="product">
        <p class="product-tagline">Hand crafted</p>
        <h1 class="product-name">JERKY BEEF</h1>
        <p class="product-flavour">WITH GARLIC, LIME AND CILANTRO</p>
      </div>
      <p class="net-weight">NET WT. 3 OZ</p>
    </div>
  </div>
</body>
</html>
```